Dietetic office: Bright Plate

I want to give my business card a modern and warm look (which attracts the eye and has a reassuring side), which links dietetics to a moment of well-being. The front and back sides must be used (not just to put the logo on the front side)

The map should be eye-catching and easy to read. I don't necessarily want to have a plain background, which I find visually weighs down the maps.
I really like the square format of a business card with rounded edges which is different from what we are used to finding (and why not take this square diagonally?), however I am not closed to another format as long as I like the style.

Who am I? Mireille, 32 years old, Dietician and passionate about food since always. I am specialized in slimming and an expert in micro nutrition, which means that I take into account not only the nutritional balance while maintaining pleasure (if foods are present in the business card, I do not want some cliché things where there would just be fruits and vegetables, but really something more global), but also the psycho-emotional dimension that I will treat with food supplements based on plants, fruits or vegetables.

-----------------------------------------------------------------------------------

 Mention to appear on the card IN FRENCH (please be careful in case of translation that the use of words is correct):

Mireille DORAN
Dietician Nutritionist
Expert in Slimming and Micro-Nutrition

Slogan: I help you lose weight sustainably with pleasure and by reconciling your events

Catchphrases: Want to lose weight? Do you like going out? Do you have a lot of events? And is pleasure on your plate important to you?

Make an appointment on Rendiplan or on 06 41 58 30 92
mireille.brightplate@exemplo-mail.fr
Address: Centre Santé Horizon, Rue des Glycines, 13990 Valbrune
www.brightplate-exemple.fr
Friendwall + Picturo Logo

- The company logo has been uploaded for your viewing. Other file formats can be made available if required.
- I would like a place for a photo of me to be possible.

Good morning,
I want to have a business card that is both lively and warm. Which will easily catch the eye while being easy to read and make people understand that I am in the field of well-being.
I like the square side in business cards (and why not use them diagonally?), or a more classic but original one.
Both the front and back sides must be used (I don't want to have the logo on just one side)
I don't want to have a plain background, but rather something more muted (I really like the suggestion from "Reed Cloud Graphic Designer" for this)
the use of logo for telephone, mail, address, rendiplan, friendwall, pictu etc is possible in order to facilitate reading

Please follow the various elements of the brief regarding the text and use the French text as it is.

I like business cards preferably square (with the possibility of using them diagonally).
The map should be eye-catching and easy to read.
It must bring pep while having softness which brings back to the well-being side
The card must be used on the front and back for the different elements (I do not want to have only the logo on the front side)
The text must correspond to the brief (be careful with the translation which can sometimes be bad)
I don't want to have a plain blue or orange background. I really like the idea of the background from "Reed Cloud Graphic Designer"

You can if you wish use symbols for contacts, telephone, rendiplan, address, fw, pictu....

Target Market(s)

mainly women between 25 and 65 years old + men around 40 years old

Contact Information for Business Card

Font styles to use
Sans Serif
Script

Colors
0054AA
0677BA
7BADD7
CADEEF
E8F1F8
0094D4
00A9DD
6FCCEA
C7EBF8
E9F6FB
00AB8E
00BBA5
67D7C9
C6EFE9
E9F9F6
FFC000
F8CF3A
FAE287
FDF2CF
FEFAEE
F0912C
F2A743
F7CA91
FBE8D2
FDF5EE

Requirements
Must have
• some pep! while being refined
Nice to have
• I really like the square format of a business card with rounded edges which is different from what we are used to finding, however I am not closed to another format as long as I like the style.
Should not have
• if foods are represented, only show fruits and vegetables (too cliché)

```html
<!DOCTYPE html>
<html lang="fr">
<head>
<meta charset="utf-8">
<title>Bright Plate – cartes de visite</title>
<link rel="stylesheet" href="https://fonts.googleapis.com/css2?family=Poppins:wght@400;500;600&family=Marcellus&family=Merriweather:wght@400&family=Allura&display=swap">
<style>
  :root {
    --bg: #d3eaf5;
    --card: #ffffff;
    --blue-deep: #0054aa;
    --blue: #0677ba;
    --blue-bright: #0094d4;
    --cyan: #00a9dd;
    --cyan-soft: #6fccea;
    --green: #00ab8e;
    --gold: #d9a522;
    --orange: #f0912c;
    --orange-soft: #f7ca91;
    --ink: #222222;
    --sans: "Poppins", sans-serif;
    --display: "Marcellus", serif;
    --serif: "Merriweather", serif;
    --script: "Allura", cursive;
  }
  * { box-sizing: border-box; margin: 0; padding: 0; }
  html, body { width: 1170px; height: 1200px; overflow: hidden; }
  body { background: var(--bg); font-family: var(--sans); color: var(--ink); position: relative; }

  .card {
    position: absolute; top: 330px; width: 540px; height: 540px;
    background: var(--card); overflow: hidden;
    box-shadow: 0 10px 24px rgba(40, 90, 120, 0.12);
  }
  .card--front { left: 30px; }
  .card--back { left: 600px; }
  .card > * { position: absolute; }

  .brand { font-family: var(--sans); font-weight: 500; color: var(--blue-bright); display: flex; align-items: center; gap: 8px; white-space: nowrap; }
  .brand__dot { width: 12px; height: 12px; border-radius: 50%; background: var(--orange); }

  .leaves--blue { background: radial-gradient(ellipse at 50% 50%, rgba(111,204,234,0.85), rgba(111,204,234,0.15) 70%, transparent 72%); }
  .leaves--orange { background: radial-gradient(ellipse at 50% 50%, rgba(247,202,145,0.9), rgba(247,202,145,0.15) 70%, transparent 72%); }

  /* front */
  .card--front .leaves--blue { left: 10px; top: -40px; width: 160px; height: 150px; }
  .card--front .brand { left: 47px; top: 140px; font-size: 38px; }
  .utensils {
    left: 392px; top: 0; width: 122px; height: 377px; border-radius: 0 0 40px 40px;
    background: linear-gradient(180deg, var(--orange) 0%, var(--blue) 30%, var(--cyan) 55%, var(--blue-deep) 80%, var(--cyan) 100%);
    opacity: 0.85;
  }
  .name {
    left: 47px; top: 244px; font-family: var(--display); font-size: 44px; line-height: 1; font-weight: 400;
    background: linear-gradient(90deg, var(--blue) 0%, var(--cyan) 40%, var(--green) 58%, var(--gold) 80%, var(--orange) 100%);
    -webkit-background-clip: text; background-clip: text; color: transparent; white-space: nowrap;
  }
  .title { left: 47px; top: 291px; font-size: 20px; font-weight: 400; line-height: 1.1; white-space: nowrap; z-index: 1; }
  .title-bar { left: 47px; top: 308px; width: 313px; height: 12px; background: var(--orange); }
  .specialty { left: 47px; top: 324px; font-family: var(--script); font-size: 23px; line-height: 1.1; white-space: nowrap; }
  .slogan { left: 47px; top: 416px; font-size: 17.5px; font-weight: 500; line-height: 1.3; }
  .card--front .leaves--orange { left: 370px; top: 430px; width: 170px; height: 150px; }

  /* back */
  .catchphrase {
    left: 47px; top: 85px; font-family: var(--serif); font-size: 27px; line-height: 1.05;
    background: linear-gradient(90deg, var(--cyan) 0%, var(--green) 55%, var(--orange) 100%);
    -webkit-background-clip: text; background-clip: text; color: transparent;
  }
  .card--back .brand { left: 250px; top: 102px; font-size: 30px; }
  .portrait-ring { left: 31px; top: 227px; width: 162px; height: 162px; border: 1px solid var(--orange); border-radius: 50%; }
  .portrait { left: 39px; top: 235px; width: 146px; height: 146px; border-radius: 50%; background: radial-gradient(circle at 50% 40%, #f3ede8, #d9d4cf); }
  .card--back .leaves--orange.top { left: 130px; top: 200px; width: 70px; height: 80px; }
  .card--back .leaves--orange.bottom { left: 50px; top: 370px; width: 90px; height: 70px; }
  .divider { left: 218px; top: 207px; width: 1px; height: 218px; background: var(--ink); }
  .booking-lead {
    left: 246px; top: 200px; font-family: var(--script); font-size: 26px; white-space: nowrap;
    background: linear-gradient(90deg, var(--blue) 0%, var(--green) 55%, var(--orange) 100%);
    -webkit-background-clip: text; background-clip: text; color: transparent;
  }
  .booking-name { left: 246px; top: 226px; font-size: 23px; font-weight: 600; color: var(--blue); }
  .contacts { left: 246px; top: 262px; list-style: none; font-size: 12.5px; line-height: 1.25; }
  .contacts li { display: flex; align-items: flex-start; gap: 8px; margin-bottom: 9px; white-space: nowrap; }
  .contacts svg { width: 13px; height: 13px; flex: none; margin-top: 1px; }
  .contacts .or { margin-bottom: 11px; }
  .social { gap: 6px !important; }
  .social__mark { width: 11px; height: 11px; margin-top: 3px; flex: none; }
  .social__mark--circle { border-radius: 50%; background: var(--blue); }
  .social__mark--square { background: var(--cyan); }
  .social__sep { margin: 0 6px; }
  .card--back .leaves--blue { left: 355px; top: 420px; width: 160px; height: 150px; }
</style>
</head>
<body>

<section class="card card--front">
  <div class="leaves leaves--blue" role="img" aria-label="Feuillage bleu décoratif"></div>
  <div class="brand"><span class="brand__dot"></span>Bright Plate</div>
  <div class="utensils" role="img" aria-label="Motif de cuillères colorées suspendues"></div>
  <h1 class="name">Mireille DORAN</h1>
  <div class="title-bar"></div>
  <p class="title">Diététicienne Nutritionniste</p>
  <p class="specialty">Expert en Minceur et Micro-Nutrition</p>
  <p class="slogan">Je vous aide à perdre du poids durablement<br>avec plaisir et en conciliant vos événements.</p>
  <div class="leaves leaves--orange" role="img" aria-label="Feuillage orange décoratif"></div>
</section>

<section class="card card--back">
  <p class="catchphrase">Do you like<br>going out?</p>
  <div class="brand"><span class="brand__dot"></span>Bright Plate</div>
  <div class="leaves leaves--orange top" role="img" aria-label="Feuillage orange décoratif"></div>
  <div class="leaves leaves--orange bottom" role="img" aria-label="Feuillage orange décoratif"></div>
  <div class="portrait-ring"></div>
  <div class="portrait" role="img" aria-label="Photo de la diététicienne"></div>
  <div class="divider"></div>
  <p class="booking-lead">Prendre rendez-vous sur</p>
  <p class="booking-name">Rendiplan</p>
  <ul class="contacts">
    <li class="or">OR</li>
    <li>
      <svg viewBox="0 0 24 24"><path fill="#0677ba" d="M6.6 10.8a15.1 15.1 0 0 0 6.6 6.6l2.2-2.2c.3-.3.7-.4 1-.2 1.1.4 2.3.6 3.6.6.6 0 1 .4 1 1V20c0 .6-.4 1-1 1A17 17 0 0 1 3 4c0-.6.4-1 1-1h3.5c.6 0 1 .4 1 1 0 1.3.2 2.5.6 3.6.1.3 0 .7-.2 1z"/></svg>
      06 41 58 30 92
    </li>
    <li>
      <svg viewBox="0 0 24 24"><path fill="#00a9dd" d="M6 2l13 11-6 .6 3.5 7.4-2.6 1.2-3.4-7.5L6 19z"/></svg>
      brightplate-exemple.fr
    </li>
    <li>
      <svg viewBox="0 0 24 24"><path fill="#0677ba" d="M2 5h20v14H2z"/><path fill="none" stroke="#fff" stroke-width="1.8" d="M2.5 5.5 12 13l9.5-7.5"/></svg>
      mireille.brightplate@exemplo-mail.fr
    </li>
    <li>
      <svg viewBox="0 0 24 24"><path fill="#00a9dd" d="M12 2a7 7 0 0 0-7 7c0 5.2 7 13 7 13s7-7.8 7-13a7 7 0 0 0-7-7zm0 9.5A2.5 2.5 0 1 1 12 6.5a2.5 2.5 0 0 1 0 5z"/></svg>
      Centre Santé Horizon, Rue des Glycines,<br>13990 Valbrune
    </li>
    <li class="social">
      <span class="social__mark social__mark--circle"></span>Brightplate
      <span class="social__sep">|</span>
      <span class="social__mark social__mark--square"></span>Brightplate
    </li>
  </ul>
  <div class="leaves leaves--blue" role="img" aria-label="Feuillage bleu décoratif"></div>
</section>

</body>
</html>
```